Business Card Design

We are a Sydney based bespoke Concierge company, providing hospitality services including Concierge staffing, catering, home dining, events, delivery, passwright, and manage desks in residential apartment services. Our website goes into more detail.

Target Market(s)

corporate clients, upscale residential clients, executives,

Industry/Entity Type

Hospitality

Contact Information for Business Card

David SouthwellDirector of Operations & Customer Experience
Larkmoor Concierge
W:www.larkmoorconcierge.net;
E;martin@larkmoorconcierge.net
M: 0491 570 213

Font styles to use
Serif

Colors
3176b5
85cae6
d2a4cc
6b449b

Requirements
Must have
• Business name
• Name
• Title
• Tel
• Email
• Website
Nice to have
• Back - facebook , twitter, instagram

```html
<!DOCTYPE html>
<html lang="en">
<head>
<meta charset="utf-8">
<title>Larkmoor Concierge – Business Cards</title>
<link rel="stylesheet" href="https://fonts.googleapis.com/css2?family=Open+Sans:wght@300;400;600;700&display=swap">
<style>
  :root {
    --backdrop: #ebe6de;
    --card-white: #ffffff;
    --ink-black: #030303;
    --band-grey: #6e6e6e;
    --olive: #a3a52b;
    --text-dark: #333333;
    --text-light: #ffffff;
  }
  * { box-sizing: border-box; margin: 0; padding: 0; }
  html, body {
    width: 983px; height: 1200px; overflow: hidden;
    background: var(--backdrop);
    font-family: "Open Sans", Arial, sans-serif;
  }
  .card {
    position: absolute;
    width: 784px; height: 470px;
    background: var(--card-white);
    box-shadow: 0 2px 8px rgba(0,0,0,0.18);
    overflow: hidden;
  }
  .card--front { left: 99px; top: 74px; }
  .card--back { left: 90px; top: 620px; }
  .card__art { position: absolute; inset: 0; }

  .wordmark {
    position: absolute;
    color: var(--text-light);
    font-weight: 300;
    text-transform: uppercase;
    line-height: 0.84;
    letter-spacing: 0.01em;
  }
  .card--front .wordmark { left: 182px; top: 48px; font-size: 64px; }
  .card--back .wordmark { left: 96px; top: 64px; font-size: 47px; }

  .front__website {
    position: absolute; left: 189px; top: 195px;
    color: var(--text-light);
    font-weight: 700; font-size: 30px;
  }
  .services {
    position: absolute; left: 189px; top: 252px;
    color: var(--text-dark); font-size: 24px;
  }
  .services__title { font-weight: 700; margin-bottom: 6px; }
  .services__list { list-style: none; }
  .services__list li { line-height: 39.5px; }
  .services__list li::before {
    content: "•"; color: var(--olive); margin-right: 8px;
  }

  .person { position: absolute; left: 96px; top: 218px; }
  .person__name { color: var(--text-light); font-weight: 700; font-size: 27px; line-height: 1.2; }
  .person__title { color: var(--text-dark); font-size: 19.5px; margin-top: 6px; }

  .contacts { position: absolute; left: 94px; top: 311px; list-style: none; }
  .contacts__item {
    display: flex; align-items: center;
    height: 43px;
    color: var(--text-dark); font-size: 26px;
  }
  .contacts__icon { width: 26px; height: 26px; margin-right: 18px; flex: none; }
</style>
</head>
<body>

<section class="card card--front" aria-label="Card front">
  <svg class="card__art" width="784" height="470" viewBox="0 0 784 470">
    <rect x="0" y="0" width="784" height="238" fill="var(--olive)"/>
    <path d="M0 0 H784 V196 H205 C105 196 22 165 0 88 Z" fill="var(--band-grey)"/>
    <path d="M0 0 H784 V184 H205 C105 184 22 150 0 73 Z" fill="var(--ink-black)"/>
  </svg>
  <div class="wordmark">Larkmoor<br>Concierge</div>
  <div class="front__website">www.larkmoorconcierge.net</div>
  <div class="services">
    <p class="services__title">Specializing in:</p>
    <ul class="services__list">
      <li>Event planning</li>
      <li>Apartment concierge services</li>
      <li>Retail centre management and corporate</li>
      <li>Lifestyle and personal concierge services</li>
    </ul>
  </div>
</section>

<section class="card card--back" aria-label="Card back">
  <svg class="card__art" width="784" height="470" viewBox="0 0 784 470">
    <defs>
      <clipPath id="header-shape">
        <path d="M0 0 H784 V127 C762 172 690 197 580 197 H0 Z"/>
      </clipPath>
      <linearGradient id="portrait-tone" x1="0" y1="0" x2="1" y2="0">
        <stop offset="0" stop-color="#050505"/>
        <stop offset="0.35" stop-color="#4a4a4a"/>
        <stop offset="1" stop-color="#8a8a8a"/>
      </linearGradient>
    </defs>
    <rect x="0" y="0" width="784" height="292" fill="var(--olive)"/>
    <path d="M0 0 H784 V142 C762 186 690 209 580 209 H0 Z" fill="var(--band-grey)"/>
    <path d="M0 0 H784 V127 C762 172 690 197 580 197 H0 Z" fill="var(--ink-black)"/>
    <rect x="462" y="0" width="322" height="200" fill="url(#portrait-tone)" clip-path="url(#header-shape)"
          role="img" aria-label="Black and white portrait of the director seated in a suit in a hotel lobby"/>
  </svg>
  <div class="wordmark">Larkmoor<br>Concierge</div>
  <div class="person">
    <p class="person__name">Martin Ashgrove</p>
    <p class="person__title">Director of Operations &amp; Customer Experience</p>
  </div>
  <ul class="contacts">
    <li class="contacts__item">
      <svg class="contacts__icon" viewBox="0 0 26 26" aria-hidden="true">
        <rect x="2" y="7" width="22" height="14" fill="none" stroke="var(--olive)" stroke-width="2"/>
        <path d="M2 7 L13 15 L24 7" fill="none" stroke="var(--olive)" stroke-width="2"/>
      </svg>
      martin@larkmoorconcierge.net
    </li>
    <li class="contacts__item">
      <svg class="contacts__icon" viewBox="0 0 26 26" aria-hidden="true">
        <rect x="7" y="2" width="12" height="22" rx="2" fill="none" stroke="var(--olive)" stroke-width="2"/>
        <line x1="11" y1="20" x2="15" y2="20" stroke="var(--olive)" stroke-width="2"/>
      </svg>
      0491 570 213
    </li>
    <li class="contacts__item">
      <svg class="contacts__icon" viewBox="0 0 26 26" aria-hidden="true">
        <circle cx="13" cy="13" r="10" fill="none" stroke="var(--olive)" stroke-width="2"/>
        <ellipse cx="13" cy="13" rx="4.5" ry="10" fill="none" stroke="var(--olive)" stroke-width="1.6"/>
        <line x1="3" y1="13" x2="23" y2="13" stroke="var(--olive)" stroke-width="1.6"/>
      </svg>
      www.larkmoorconcierge.net
    </li>
  </ul>
</section>

</body>
</html>
```